Design some Business Cards

Need some business cards made for new venture - website is varimest.com. I want to incorporate (in some fashion):

- logo (provided with name, and alone)
- website <p> font (Arvo )

Brian T. Holloway
BH VARIMEST
819 N. Garrick Ave. 3rd Floor
Chicago, IL 60647
brianh@varimest.com
(312) 448-2096
varimest.com

I am not very creative, hence the contest. Feel free to add design elements, but keep things consistent with the website (naturally). I am indifferent to one side vs. two-sided business card. I will be using PressNova, so you will want to use their Illustrator (or photoshop) templates located here:

http://www.pressnova-example.com/pn/ns/prodir/FileResources.aspx?pf_id=C41&selectedTab=0

The work product will be an Illustrator or Photoshop file, using the templates, with the winning design.

```html
<!DOCTYPE html>
<html lang="en">
<head>
<meta charset="utf-8">
<title>Varimest Business Cards</title>
<link href="https://fonts.googleapis.com/css2?family=Arvo:wght@400;700&family=Poppins:wght@400;500&display=swap" rel="stylesheet">
<style>
  :root {
    --page-bg: #e9e6e1;
    --card-dark: #141414;
    --card-dark-edge: #232323;
    --card-light-top: #fafafa;
    --card-light-bottom: #dedede;
    --ink-dark: #1a1a1a;
    --ink-light: #f2f2f2;
    --ink-grey: #6e6e6e;
    --ink-name: #4a4a4a;
  }
  * { margin: 0; padding: 0; box-sizing: border-box; }
  html, body { width: 1200px; height: 900px; overflow: hidden; }
  body {
    background: var(--page-bg);
    position: relative;
    font-family: 'Poppins', sans-serif;
  }
  .card {
    position: absolute;
    width: 680px;
    height: 388px;
    border-radius: 4px;
    box-shadow: 0 14px 30px rgba(0,0,0,0.22);
  }
  .card-front {
    left: 120px;
    top: 52px;
    background: linear-gradient(160deg, var(--card-dark-edge), var(--card-dark));
  }
  .card-back {
    left: 400px;
    top: 462px;
    background: linear-gradient(170deg, var(--card-light-top), var(--card-light-bottom));
  }
  .brand {
    position: absolute;
    display: flex;
    align-items: center;
    gap: 14px;
  }
  .brand-dot {
    width: 34px;
    height: 34px;
    border-radius: 50%;
  }
  .brand-name {
    font-family: 'Arvo', serif;
    font-weight: 400;
    font-size: 40px;
    line-height: 1;
  }
  .card-front .brand { left: 44px; bottom: 44px; }
  .card-front .brand-dot { background: var(--ink-light); }
  .card-front .brand-name { color: var(--ink-light); }
  .card-back .brand { right: 44px; top: 40px; }
  .card-back .brand-dot { background: var(--ink-dark); }
  .card-back .brand-name { color: var(--ink-dark); }
  .contact {
    position: absolute;
    left: 44px;
    bottom: 38px;
    color: var(--ink-grey);
  }
  .contact-name {
    font-size: 24px;
    font-weight: 500;
    color: var(--ink-name);
    line-height: 1.2;
  }
  .contact-title {
    font-size: 13px;
    letter-spacing: 0.12em;
    margin-bottom: 10px;
  }
  .contact-address { font-size: 15px; margin-bottom: 6px; }
  .contact-lines {
    display: flex;
    align-items: center;
    gap: 10px;
    font-size: 14px;
  }
  .contact-item { display: flex; align-items: center; gap: 6px; }
  .contact-item svg { width: 16px; height: 16px; }
  .sep { color: var(--ink-grey); }
</style>
</head>
<body>
  <div class="card card-front">
    <div class="brand">
      <span class="brand-dot"></span>
      <span class="brand-name">varimest</span>
    </div>
  </div>

  <div class="card card-back">
    <div class="brand">
      <span class="brand-dot"></span>
      <span class="brand-name">varimest</span>
    </div>
    <div class="contact">
      <div class="contact-name">Brian T. Holloway</div>
      <div class="contact-title">BH VARIMEST</div>
      <div class="contact-address">819 N. Garrick Ave. 3rd Floor, Chicago, IL 60647</div>
      <div class="contact-lines">
        <span class="contact-item">
          <svg viewBox="0 0 16 16" aria-hidden="true"><circle cx="8" cy="8" r="8" fill="#6e6e6e"/><path d="M5.5 4.5l1.4 0 .6 1.8-.9.7a5 5 0 0 0 2.4 2.4l.7-.9 1.8.6v1.4c0 .4-.3.6-.7.6A6.3 6.3 0 0 1 4.9 5.2c0-.4.2-.7.6-.7z" fill="#f2f2f2"/></svg>
          (312) 448-2096
        </span>
        <span class="sep">|</span>
        <span class="contact-item">
          <svg viewBox="0 0 16 16" aria-hidden="true"><circle cx="8" cy="8" r="8" fill="#6e6e6e"/><circle cx="8" cy="8" r="4.5" fill="none" stroke="#f2f2f2" stroke-width="1"/><ellipse cx="8" cy="8" rx="2" ry="4.5" fill="none" stroke="#f2f2f2" stroke-width="1"/><line x1="3.5" y1="8" x2="12.5" y2="8" stroke="#f2f2f2" stroke-width="1"/></svg>
          varimest.com
        </span>
        <span class="sep">|</span>
        <span class="contact-item">
          <svg viewBox="0 0 16 16" aria-hidden="true"><circle cx="8" cy="8" r="8" fill="#6e6e6e"/><rect x="4" y="5.2" width="8" height="5.6" fill="none" stroke="#f2f2f2" stroke-width="1"/><path d="M4 5.4l4 3 4-3" fill="none" stroke="#f2f2f2" stroke-width="1"/></svg>
          brianh@varimest.com
        </span>
      </div>
    </div>
  </div>
</body>
</html>
```